Talvok Engineering Business card Design

We need to make business cards for our NDT and inspection company. The company is called Talvok Engineering. We want a professional modern feel business card. We have just completed the remaking of our website and would like to have business cards with the same feel and colours. The final design should communicate professionalism and cutting edge tech.

Target Market(s)

We sell to B2B Business clients. Our customer is an engineer or decision maker in the mechanical engineering / Oil and gas field.

Contact Information for Business Card

Please see the current business cards that we have uploaded to get the details. You can also look at our Website www.talvok-eng.example for more.

Requirements
Must have
• Less is more
Nice to have
• Less is more

```html
<!DOCTYPE html>
<html lang="en">
<head>
<meta charset="utf-8">
<title>Talvok Engineering – Business Card</title>
<link rel="stylesheet" href="https://fonts.googleapis.com/css2?family=Oswald:wght@500;600&family=Roboto:wght@400;500&display=swap">
<style>
  :root {
    --red: #a90f15;
    --red-deep: #8e0c11;
    --navy: #1f3068;
    --white: #ffffff;
    --soft: #e6e6e6;
    --bg: #3a3b3d;
  }
  * { box-sizing: border-box; margin: 0; padding: 0; }
  html, body { width: 1200px; height: 960px; overflow: hidden; }
  body {
    background: var(--bg);
    font-family: "Roboto", Arial, sans-serif;
    position: relative;
  }
  .card {
    position: absolute;
    left: 250px;
    width: 700px;
    height: 400px;
    border-radius: 22px;
    overflow: hidden;
    box-shadow: 0 12px 28px rgba(0,0,0,.45);
  }
  /* ---------- back: services ---------- */
  .card-back { top: 40px; background: var(--red); color: var(--white); }
  .back-brand {
    position: absolute; left: 40px; top: 0; width: 320px; height: 400px;
    display: flex; align-items: center; justify-content: center; gap: 14px;
  }
  .brand-dot { width: 22px; height: 22px; border-radius: 50%; flex: none; }
  .card-back .brand-dot { background: var(--white); }
  .brand-name { font-family: "Roboto", Arial, sans-serif; font-weight: 500; font-size: 30px; letter-spacing: .3px; }
  .back-divider {
    position: absolute; left: 380px; top: 70px; width: 1px; height: 260px;
    background: rgba(255,255,255,.75);
  }
  .service-list {
    position: absolute; left: 412px; top: 72px; list-style: none;
    font-size: 16px; line-height: 23px;
  }
  .service-list li::before {
    content: ""; display: inline-block; width: 6px; height: 6px; border-radius: 50%;
    background: var(--white); margin-right: 10px; vertical-align: middle;
  }
  /* ---------- front: contact ---------- */
  .card-front { top: 520px; background: var(--navy); color: var(--white); }
  .front-shape { position: absolute; inset: 0; }
  .front-brand {
    position: absolute; left: 380px; top: 105px;
    display: flex; align-items: center; gap: 12px; color: var(--navy);
  }
  .card-front .brand-dot { background: var(--red); }
  .front-brand .brand-name { font-size: 28px; }
  .contact {
    position: absolute; left: 44px; top: 180px;
  }
  .person-name {
    font-family: "Oswald", Impact, sans-serif; font-weight: 600;
    font-size: 30px; line-height: 32px; text-transform: uppercase; letter-spacing: .3px;
  }
  .person-title { font-size: 15px; letter-spacing: .8px; text-transform: uppercase; margin-bottom: 16px; }
  .address { font-size: 17px; line-height: 22px; margin-bottom: 12px; }
  .contact-lines { list-style: none; font-size: 17px; line-height: 24px; }
  .contact-lines li { display: flex; align-items: center; gap: 10px; }
  .contact-lines svg { width: 14px; height: 14px; fill: var(--white); flex: none; }
</style>
</head>
<body>

<section class="card card-back" aria-label="Card back: services">
  <div class="back-brand">
    <span class="brand-dot"></span>
    <span class="brand-name">Talvok Engineering</span>
  </div>
  <div class="back-divider"></div>
  <ul class="service-list">
    <li>API 653 Tank Inspections</li>
    <li>API 570 Pipeline Inspections</li>
    <li>API 510 Pressure Vessel Inspections</li>
    <li>Welding Inspections</li>
    <li>Electrical Inspections</li>
    <li>OCTG Inspections</li>
    <li>Lifting Equipment Inspections</li>
    <li>Non-Destructive Testing</li>
    <li>UT / PT / MT / RT / VT</li>
    <li>Advanced NDT</li>
    <li>PAUT / MFL / ILI</li>
    <li>Engineering Projects</li>
  </ul>
</section>

<section class="card card-front" aria-label="Card front: contact">
  <svg class="front-shape" viewBox="0 0 700 400" preserveAspectRatio="none" aria-hidden="true">
    <path d="M300,0 C310,230 500,355 700,352 L700,0 Z" fill="var(--red)"/>
    <path d="M318,0 C345,205 520,330 700,334 L700,0 Z" fill="var(--white)"/>
  </svg>
  <div class="front-brand">
    <span class="brand-dot"></span>
    <span class="brand-name">Talvok Engineering</span>
  </div>
  <div class="contact">
    <h1 class="person-name">Daniel Okafor</h1>
    <p class="person-title">President</p>
    <p class="address">Harbour Lane, Block 7<br>P.O. BOX 40512-10200<br>Kestrel Bay</p>
    <ul class="contact-lines">
      <li><svg viewBox="0 0 16 16"><path d="M3.6 1.2l2.3 2.9-1.4 1.8c.9 2 2.6 3.7 4.6 4.6l1.8-1.4 2.9 2.3-1.2 2.8C7 14 2 9 1 2.4z"/></svg>+000 55 482 1390/1</li>
      <li><svg viewBox="0 0 16 16"><path d="M1 3h14v10H1z M1.8 3.8L8 9l6.2-5.2" fill="none" stroke="#fff" stroke-width="1.6"/></svg>info@talvok-eng.example</li>
      <li><svg viewBox="0 0 16 16"><circle cx="8" cy="8" r="7"/><path d="M1 8h14M8 1c-3 3.5-3 10.5 0 14M8 1c3 3.5 3 10.5 0 14" stroke="#1f3068" stroke-width="1.2" fill="none"/></svg>talvok-eng.example</li>
    </ul>
  </div>
</section>

</body>
</html>
```